I want a business card that is going to show a creative spark but without limiting me to an industry. Something edgy but that wont go out of date. I want it state My business name Serafina Loire, profession - Professional Makeup Artist contact number and email

My service is to provide makeup services from bridal, fashion, photography, film, TV and so on. It is creative and different so i want that to be reflected.

I would like the card double sided.
Updates

 I would LOVE a background on my card something like this image... i can supply an image to be formed like this

Please use the image uploaded

Can we try using the image provided on one side of the card and then writing and details on the other side

Target Market(s)

I am targeting a wide range of people from Creative directors to the individual eg. bride

Industry/Entity Type

Business

Requirements
Must have
• Name: Delphine Hartwell
contact numbe 0417853120
email address:info@serafinaloire.com
website: www.serafinaloire.com
One of the images attached

professional makeup artist / hair stylist

I want it to show creativity
Nice to have
• logo, Double-sided card
Should not have
• the design should not use tradional style. Or images that are not my own

```html
<!DOCTYPE html>
<html lang="en">
<head>
<meta charset="utf-8">
<title>Serafina Loire — Business Card</title>
<link rel="stylesheet" href="https://fonts.googleapis.com/css2?family=Signika:wght@300;400&family=Share+Tech+Mono&display=swap">
<style>
  :root {
    --backdrop: #d6d6d6;
    --card-top: #242424;
    --card-bottom: #0e0e0e;
    --ink-light: #f2f2f2;
    --ink-muted: #d8d8d8;
    --ink-deep: #050505;
  }
  * { margin: 0; padding: 0; box-sizing: border-box; }
  html, body {
    width: 1200px;
    height: 895px;
    overflow: hidden;
    background: var(--backdrop);
  }
  .canvas {
    position: relative;
    width: 1200px;
    height: 895px;
  }
  .card {
    position: absolute;
    top: 302px;
    width: 574px;
    height: 344px;
    border-radius: 43px;
    background: radial-gradient(ellipse at 60% 10%, var(--card-top) 0%, #181818 45%, var(--card-bottom) 100%);
    overflow: hidden;
  }
  .card--front { left: 16px; }
  .card--back { left: 604px; }

  /* Front */
  .front-name {
    position: absolute;
    left: 0; right: 0;
    top: 180px;
    text-align: center;
    font-family: "Signika", sans-serif;
    font-weight: 400;
    font-size: 46px;
    letter-spacing: 3px;
    color: var(--ink-deep);
  }

  /* Back */
  .back-brand {
    position: absolute;
    left: 74px;
    top: 95px;
    font-family: "Signika", sans-serif;
    font-weight: 400;
    font-size: 23px;
    letter-spacing: 1.8px;
    color: var(--ink-light);
  }
  .details {
    position: absolute;
    right: 74px;
    top: 198px;
    text-align: right;
  }
  .details__name {
    font-family: "Signika", sans-serif;
    font-weight: 300;
    font-size: 22px;
    line-height: 26px;
    color: var(--ink-light);
  }
  .details__role {
    font-family: "Share Tech Mono", monospace;
    font-size: 11.5px;
    letter-spacing: 2.7px;
    line-height: 16px;
    color: var(--ink-muted);
    margin-right: -3px;
  }
  .contact {
    list-style: none;
    margin-top: 17px;
    font-family: "Share Tech Mono", monospace;
    font-size: 11.5px;
    letter-spacing: 3.1px;
    line-height: 15px;
    color: var(--ink-muted);
  }
  .contact__item {
    display: flex;
    justify-content: flex-end;
    align-items: center;
    gap: 12px;
  }
  .contact__phone { letter-spacing: 2.4px; }
  .contact__icon { width: 13px; height: 11px; fill: var(--ink-muted); }
</style>
</head>
<body>
<main class="canvas">
  <section class="card card--front" aria-label="Card front">
    <p class="front-name">Serafina Loire</p>
  </section>

  <section class="card card--back" aria-label="Card back">
    <p class="back-brand">Serafina Loire</p>

    <div class="details">
      <p class="details__name">Serafina Loire</p>
      <p class="details__role">PROFESSIONAL MAKEUP ARTIST</p>
      <ul class="contact">
        <li class="contact__item">
          <span class="contact__phone">0417 853 120</span>
          <svg class="contact__icon" viewBox="0 0 13 11" aria-hidden="true">
            <path d="M0 3.5 C0 1 3 0 6.5 0 S13 1 13 3.5 L10 4 L9.5 2.5 C8 2 5 2 3.5 2.5 L3 4 Z"/>
            <path d="M2.5 5 L10.5 5 L12 11 L1 11 Z"/>
          </svg>
        </li>
        <li class="contact__item">
          <span>STUDIO@SERAFINALOIRE.COM.AU</span>
          <svg class="contact__icon" viewBox="0 0 13 11" aria-hidden="true">
            <path d="M0 4 L6.5 0 L13 4 L13 11 L0 11 Z"/>
            <path d="M1.5 4.5 L6.5 7.5 L11.5 4.5" fill="none" stroke="#141414" stroke-width="1"/>
          </svg>
        </li>
      </ul>
    </div>
  </section>
</main>
</body>
</html>
```